University Student Business Card

Looking for a professional university student business card. Student is studying business with a focus on marketing. Some combination using a monogram and/or full name on the front with full name, university details and contact information on the back. Card should be modern design for a young professional. Prefer use of royal blue, black and white but am open to other uses of colour palette if it reinforces young/trendy style. Initials for a monogram are: KM. Full details will be provided in private consultation with designer(s).

Target Market(s)

Professional business people, marketers, advertisers, consultants

Industry/Entity Type

Business, marketing

Contact Information for Business Card

Monogram or personal logo, full name, university name, program of study, phone number, email address, linkedin address

Other font styles liked:
• Open to suggestion to fulfill above requirements

Colors
0054AA
0677BA
7BADD7
CADEEF
E8F1F8

Requirements
Must have
• Monogram using letters K and M, and incorporate the business card details listed in the brief (specific details including personal contact info will be shared with successful designer to ensure privacy)
Nice to have
• Personal brand using monogram or personal logo (not a business logo)

```html
<!DOCTYPE html>
<html lang="en">
<head>
<meta charset="utf-8">
<title>KM Student Business Card</title>
<link href="https://fonts.googleapis.com/css2?family=Open+Sans:wght@400;600;700&display=swap" rel="stylesheet">
<style>
  :root{
    --stage:#eef1f4;
    --blue-deep:#134d7c;
    --blue-mid:#2369a0;
    --blue-wave:#4a90c0;
    --blue-bright:#2fb0e6;
    --ink:#1e1e1e;
    --ink-faint:#262626;
    --white:#ffffff;
    --orange:#f0922b;
    --contact-blue:#6ec3ea;
    --web-yellow:#f3e4a6;
    --rule-gold:#c9a24a;
  }
  *{margin:0;padding:0;box-sizing:border-box}
  html,body{width:1200px;height:817px;overflow:hidden;background:var(--stage)}
  body{position:relative;font-family:"Open Sans",sans-serif}
  .card{position:absolute;width:495px;height:314px;overflow:hidden}
  .card-front{left:205px;top:115px;
    background:radial-gradient(circle at 45% 40%,var(--blue-mid) 0%,var(--blue-deep) 85%);z-index:2}
  .card-back{left:389px;top:401px;background:var(--ink);z-index:1}

  .wave-area{position:absolute;left:0;width:100%}
  .card-front .wave-area{bottom:0;height:80px;
    background:linear-gradient(100deg,var(--blue-bright) 0%,var(--blue-wave) 45%,var(--ink) 100%)}
  .card-back .wave-area{top:0;height:48px;
    background:linear-gradient(100deg,var(--blue-wave) 0%,var(--blue-bright) 60%,var(--blue-wave) 100%)}

  .monogram{position:absolute;left:110px;top:45px;font-size:120px;font-weight:700;
    color:var(--white);letter-spacing:2px;line-height:1}
  .university-name{position:absolute;left:177px;top:190px;font-size:15px;font-weight:700;
    color:var(--white);letter-spacing:.5px}

  .monogram-faint{position:absolute;left:40px;top:50px;font-size:230px;font-weight:700;
    color:var(--ink-faint);line-height:1;letter-spacing:4px}
  .profile-photo{position:absolute;left:364px;top:55px;width:54px;height:54px;border-radius:50%;
    background:radial-gradient(circle at 50% 45%,#f4f6f8 0%,#d9dee3 100%)}
  .person-name{position:absolute;right:74px;top:106px;font-size:20px;color:var(--orange);font-weight:400}
  .person-role{position:absolute;right:76px;top:137px;font-size:11px;color:var(--white)}
  .contact{position:absolute;left:71px;top:176px;padding-left:13px;border-left:1px solid var(--rule-gold);
    height:89px}
  .contact-head{font-size:10.5px;color:var(--white);line-height:12px;margin-top:-2px}
  .contact-line{font-size:11px;color:var(--contact-blue);line-height:14.5px;letter-spacing:.4px}
  .contact-line:first-of-type{margin-top:4px}
  .contact-web{font-size:11.5px;color:var(--web-yellow);margin-top:3px}
</style>
</head>
<body>
  <section class="card card-front" aria-label="Card front">
    <div class="wave-area" role="img" aria-label="Decorative blue and black wave band"></div>
    <div class="monogram">KM</div>
    <div class="university-name">UNIVERSITY NAME</div>
  </section>

  <section class="card card-back" aria-label="Card back">
    <div class="monogram-faint">KM</div>
    <div class="wave-area" role="img" aria-label="Decorative blue wave band"></div>
    <div class="profile-photo" role="img" aria-label="Profile photo of the student"></div>
    <div class="person-name">Full Name</div>
    <div class="person-role">Designation</div>
    <div class="contact">
      <p class="contact-head">University Details and<br>Contact information</p>
      <p class="contact-line">Elm Row No. 14 Northfield</p>
      <p class="contact-line">041-2290-5531-6604</p>
      <p class="contact-line">hello@kmstudies.example</p>
      <p class="contact-web">kmstudies.example</p>
    </div>
  </section>
</body>
</html>
```